Company Work Van Design

I am requiring designs for the company work van. The van is a White 2015 Corvane Brisk twin turbo short wheel base. I require all my details on the van. VTRA: 582 4036 M: 0471 865 302 Harbourline Waterproofing Pty Ltd, On the sides i require some dot points for examples of jobs i do. E.g Bathrooms, Balconies, Retaining Walls. Commercial, Residential. Be creative. I will keep updating the project with other details.

Industry/Entity Type

It Company

Colors
cee9f5
85cae6
34a7d8
0493ce
0356a4
3277b5
85acd3
d0dfed
ffffff

```html
<!DOCTYPE html>
<html lang="en">
<head>
<meta charset="utf-8">
<title>Van Back Side – Harbourline Waterproofing</title>
<link href="https://fonts.googleapis.com/css2?family=Questrial&family=Archivo:wght@700;800&display=swap" rel="stylesheet">
<style>
  :root {
    --page: #ffffff;
    --panel: #f1f1f3;
    --glass: #ffffff;
    --trim: #ffffff;
    --ink: #1a1a1a;
    --brand-grey: #6d777c;
    --brand-blue: #0356a4;
    --badge-chrome: #7a7c80;
    --icon-grey: #b9b9bb;
    --seam: #e2e2e6;
  }
  html, body {
    margin: 0;
    padding: 0;
    width: 1200px;
    height: 900px;
    overflow: hidden;
    background: var(--page);
  }
  .artboard {
    position: relative;
    width: 1200px;
    height: 900px;
  }
  .view-title {
    position: absolute;
    top: 54px;
    left: 0;
    width: 1200px;
    margin: 0;
    text-align: center;
    font-family: "Questrial", sans-serif;
    font-weight: 400;
    font-size: 23px;
    letter-spacing: 0.5px;
    color: var(--ink);
  }
  .van-rear {
    position: absolute;
    top: 0;
    left: 0;
  }
  .door-panel { fill: var(--panel); }
  .rear-glass, .brake-light, .handle-recess, .bumper-step, .plate-recess { fill: var(--glass); }
  .door-seam { stroke: var(--seam); stroke-width: 1.5; }
  .wiper-arm { stroke: var(--trim); stroke-width: 9; stroke-linecap: round; }
  .wiper-pivot { fill: var(--trim); }
  .model-badge {
    font-family: "Archivo", sans-serif;
    font-weight: 800;
    font-size: 19px;
    fill: var(--badge-chrome);
    letter-spacing: 0.5px;
  }
  .brand-name {
    font-family: "Archivo", sans-serif;
    font-weight: 700;
    fill: var(--brand-grey);
  }
  .brand-mark { fill: var(--brand-blue); }
  .phone-number {
    font-family: "Archivo", sans-serif;
    font-weight: 800;
    font-size: 44px;
    fill: var(--ink);
  }
  .phone-icon { fill: var(--icon-grey); }
  .phone-screen { fill: var(--panel); }
  .licence-badge { fill: var(--trim); stroke: var(--ink); stroke-width: 2; }
</style>
</head>
<body>
<main class="artboard">
  <h1 class="view-title">Van Back Side</h1>

  <svg class="van-rear" width="1200" height="900" viewBox="0 0 1200 900" aria-label="Rear doors of the work van with company details">
    <!-- rear doors -->
    <path class="door-panel" d="M290 122 L600 114 L910 118 Q946 120 948 160 L940 740 Q936 786 890 786 L330 786 Q284 786 282 742 L254 165 Q252 124 290 122 Z"/>
    <line class="door-seam" x1="600" y1="114" x2="600" y2="786"/>

    <!-- glass and lights -->
    <rect class="brake-light" x="467" y="123" width="111" height="37" rx="12"/>
    <path class="rear-glass" d="M318 168 L878 168 Q908 168 908 198 L908 410 Q908 442 876 446 L600 472 L326 444 Q288 440 288 404 L288 198 Q288 168 318 168 Z"/>

    <!-- wipers -->
    <line class="wiper-arm" x1="306" y1="436" x2="370" y2="508"/>
    <circle class="wiper-pivot" cx="372" cy="511" r="9"/>
    <line class="wiper-arm" x1="660" y1="466" x2="696" y2="508"/>
    <circle class="wiper-pivot" cx="698" cy="511" r="9"/>

    <!-- model badges -->
    <text class="model-badge" x="297" y="564">BRISK</text>
    <text class="model-badge" x="908" y="567" text-anchor="end">CORVANE</text>

    <!-- handle, bumper step, plate -->
    <path class="handle-recess" d="M424 543 L460 543 Q480 536 500 543 L548 543 Q555 543 555 550 L555 577 Q555 584 548 584 L500 584 Q480 591 460 584 L424 584 Q416 584 416 577 L416 550 Q416 543 424 543 Z"/>
    <path class="bumper-step" d="M318 662 L560 666 Q578 668 576 682 L572 692 Q570 697 560 697 L316 690 Q308 690 309 680 L312 668 Q313 662 318 662 Z"/>
    <rect class="plate-recess" x="367" y="701" width="156" height="56" rx="4"/>

    <!-- company name -->
    <circle class="brand-mark" cx="664" cy="610" r="26"/>
    <text class="brand-name" x="700" y="612" font-size="27">HARBOURLINE</text>
    <text class="brand-name" x="701" y="633" font-size="15" letter-spacing="1.5">WATERPROOFING</text>
    <text class="brand-name" x="748" y="649" font-size="10" letter-spacing="2">· PTY · LTD ·</text>

    <!-- mobile -->
    <rect class="phone-icon" x="604" y="675" width="19" height="29" rx="5"/>
    <rect class="phone-screen" x="608" y="680" width="11" height="16" rx="2"/>
    <text class="phone-number" x="632" y="704">0471 865 302</text>

    <!-- licence badge -->
    <rect class="licence-badge" x="718" y="720" width="56" height="50"/>
  </svg>
</main>
</body>
</html>
```